Website Kestrel Outdoor

Hi I'm looking for a simple design for a new website. It's outdoor products mainly in category, Boat, Tarpaulin, Fishing, Golf. I have include image and text for 8 products + presentation etc. I want a simple and modern site + fast + Mobile. Wordpress. I'm going to sell through Quorvin so I don't need any WooCommerce but a buy button to Quorvin. I haven set up the Quorvin account yet. My logo i s grey and orange. My goal is to sell in Quorvin US and later EU.

```html
<!DOCTYPE html>
<html lang="en">
<head>
<meta charset="utf-8">
<title>Kestrel Outdoor</title>
<link href="https://fonts.googleapis.com/css2?family=Jost:wght@400;500;600&display=swap" rel="stylesheet">
<style>
:root{
  --orange:#f7931e;
  --dark:#4a4a4a;
  --mid:#808080;
  --text:#333333;
  --muted:#5a5a5a;
  --light:#f8f8f8;
  --card:#eeeeee;
  --white:#ffffff;
}
*{box-sizing:border-box;margin:0;padding:0}
html,body{width:1200px;height:2178px;overflow:hidden}
body{font-family:'Jost',sans-serif;color:var(--text);background:var(--white);position:relative}
.abs{position:absolute}
.btn{position:absolute;display:flex;align-items:center;justify-content:center;border-radius:16px;font-size:11px;font-weight:500;color:var(--white);letter-spacing:.3px}
.btn-orange{background:var(--orange)}
.btn-dark{background:var(--dark)}

/* header */
.site-header{position:absolute;left:0;top:0;width:1200px;height:93px;background:var(--white);border-bottom:1px solid #e5e5e5}
.brand{position:absolute;left:200px;top:30px;display:flex;align-items:center;gap:8px}
.brand-mark{width:22px;height:22px;border-radius:50%;background:var(--mid)}
.brand-name{font-size:19px;font-weight:600;color:var(--orange);letter-spacing:1px;line-height:1}
.top-contact{position:absolute;top:17px;left:647px;display:flex;gap:10px;font-size:11px;font-weight:500;align-items:center}
.top-contact span{display:flex;align-items:center;gap:4px}
.social{position:absolute;display:flex;gap:5px}
.social i{display:block;width:29px;height:29px;border-radius:50%;background:var(--mid)}
.social i.on{background:var(--orange)}
.main-nav{position:absolute;left:392px;top:55px;display:flex;font-size:11px;font-weight:500}
.main-nav a{color:var(--text);text-decoration:none;margin-right:26px}
.main-nav a.active{color:var(--orange)}

/* hero */
.hero{position:absolute;left:0;top:93px;width:1200px;height:407px;background:var(--mid)}
.hero-photo{position:absolute;left:381px;top:0;width:819px;height:407px;background:linear-gradient(90deg,#4f7a2e 0%,#5f8a38 45%,#8a8a8a 70%,#c9c9c9 100%)}
.hero h1{position:absolute;left:200px;top:106px;width:480px;font-size:37px;line-height:45px;font-weight:500;color:var(--white)}
.dots{position:absolute;left:372px;top:365px;display:flex;gap:4px}
.dots i{width:9px;height:9px;border-radius:50%;border:1px solid var(--white)}
.dots i.on{background:var(--white)}

/* categories */
.categories{position:absolute;left:0;top:500px;width:1200px;height:275px;background:var(--dark)}
.section-title{position:absolute;width:100%;text-align:center;font-size:32px;font-weight:500}
.underline{position:absolute;height:2px;width:50px;background:var(--orange)}
.cat{position:absolute;top:127px;width:120px;text-align:center}
.cat-ring{width:76px;height:76px;margin:0 auto;border:1.5px solid var(--orange);border-radius:50%;display:flex;align-items:center;justify-content:center}
.cat-label{margin-top:10px;color:var(--orange);font-size:15px;font-weight:500}

/* featured */
.featured{position:absolute;left:0;top:775px;width:1200px;height:469px;background:var(--white)}
.featured-side{position:absolute;left:0;top:0;width:588px;height:469px;background:var(--mid)}
.tabs{position:absolute;top:67px;font-size:11px;font-weight:500}
.product-img{position:absolute;top:126px;width:250px;height:220px;background:var(--card)}
.product-img div{position:absolute;left:60px;top:30px;width:130px;height:160px;border-radius:10px}
.product-name{position:absolute;top:356px;width:250px;text-align:center;font-size:12px;font-weight:500;letter-spacing:.4px;color:var(--text)}
.arrow-btn{position:absolute;top:221px;width:30px;height:30px;border-radius:50%;background:var(--mid);border:1.5px solid var(--orange);display:flex;align-items:center;justify-content:center}

/* blogs */
.blogs{position:absolute;left:0;top:1244px;width:1200px;height:622px;background:var(--light)}
.blog-img{position:absolute}
.blog-title{position:absolute;font-size:15px;line-height:17px;font-weight:500;color:var(--text)}
.blog-text{position:absolute;font-size:11.5px;line-height:13.5px;color:var(--muted)}
.read-more{position:absolute;font-size:11.5px;font-weight:500;color:var(--orange)}
.blog-box{position:absolute;left:456px;top:364px;width:287px;height:150px;background:var(--light);text-align:center}

/* footer */
.site-footer{position:absolute;left:0;top:1866px;width:1200px;height:312px;background:var(--dark);color:var(--white)}
.footer-title{position:absolute;font-size:15px;font-weight:500}
.footer-text{position:absolute;font-size:10px;line-height:15px;color:#bdbdbd}
.quick-links{position:absolute;left:818px;top:93px;font-size:10px;line-height:15px;color:#bdbdbd}
.divider{position:absolute;left:200px;top:247px;width:800px;height:1px;background:#6a6a6a}
.copyright{position:absolute;top:273px;width:100%;text-align:center;font-size:9.5px;color:#cfcfcf}
</style>
</head>
<body>

<header class="site-header">
  <div class="brand"><span class="brand-mark"></span><span class="brand-name">KESTREL OUTDOOR</span></div>
  <div class="top-contact">
    <span><svg width="10" height="10" viewBox="0 0 24 24"><path d="M6 3l3 5-2 2a12 12 0 006 6l2-2 5 3-2 4C10 21 3 14 3 5z" fill="none" stroke="#f7931e" stroke-width="2"/></svg>123-456-7890</span>
    <span><svg width="10" height="10" viewBox="0 0 24 24"><rect x="3" y="6" width="18" height="13" rx="2" fill="#f7931e"/></svg>info@kestreloutdoor.com</span>
  </div>
  <div class="social" style="left:902px;top:10px"><i aria-label="Social link"></i><i class="on" aria-label="Social link"></i><i aria-label="Social link"></i></div>
  <nav class="main-nav">
    <a class="active">Home</a><a>About Us</a><a>Boat</a><a>Tarpaulin</a><a>Fishing</a><a>Golf</a><a>Blog</a><a>Contact Us</a>
  </nav>
  <div class="btn btn-orange" style="left:874px;top:47px;width:125px;height:31px">Buy On Quorvin</div>
</header>

<section class="hero">
  <div class="hero-photo" role="img" aria-label="Golfer's gloved hand wiping a golf ball with a towel on a green"></div>
  <h1>Lorem Ipsum is simply dummy text of the printing and typesetting</h1>
  <div class="btn btn-orange" style="left:200px;top:263px;width:125px;height:31px">Buy On Quorvin</div>
  <div class="dots"><i></i><i class="on"></i><i></i><i></i></div>
</section>

<section class="categories">
  <h2 class="section-title" style="top:44px;color:var(--white)">Shop by category</h2>
  <div class="underline" style="left:575px;top:94px"></div>
  <div class="cat" style="left:230px"><div class="cat-ring" role="img" aria-label="Boat outline icon"><svg width="50" height="30" viewBox="0 0 50 30"><path d="M3 16h44l-6 10H9z M14 16l6-8h14l6 8" fill="none" stroke="#bbb" stroke-width="1"/></svg></div><div class="cat-label">Boat</div></div>
  <div class="cat" style="left:436px"><div class="cat-ring" role="img" aria-label="Tarpaulin outline icon"><svg width="50" height="30" viewBox="0 0 50 30"><path d="M5 18l10-14h24l6 14z M10 18v8 M40 18v8" fill="none" stroke="#bbb" stroke-width="1"/></svg></div><div class="cat-label">Tarpaulin</div></div>
  <div class="cat" style="left:643px"><div class="cat-ring" role="img" aria-label="Tent outline icon"><svg width="50" height="36" viewBox="0 0 50 36"><path d="M4 20L20 4l24 18-16 12z M28 34l8-22" fill="none" stroke="#bbb" stroke-width="1"/></svg></div><div class="cat-label">Outdoor</div></div>
  <div class="cat" style="left:849px"><div class="cat-ring" role="img" aria-label="House outline icon"><svg width="50" height="44" viewBox="0 0 50 44"><path d="M4 20L25 2l21 18 M9 16v26h12V28h8v14h12V16" fill="none" stroke="#bbb" stroke-width="1.5"/></svg></div><div class="cat-label">Indoor</div></div>
</section>

<section class="featured">
  <div class="featured-side"></div>
  <h2 class="abs" style="left:198px;top:45px;font-size:32px;font-weight:500;color:var(--white)">Featured products</h2>
  <div class="underline" style="left:200px;top:93px"></div>
  <div class="tabs" style="left:755px">All</div>
  <div class="tabs" style="left:795px;color:var(--orange)">Boat</div>
  <div class="tabs" style="left:844px">Tarpaulin</div>
  <div class="tabs" style="left:916px">Fishing</div>
  <div class="tabs" style="left:978px">Golf</div>

  <div class="product-img" style="left:200px"><div role="img" aria-label="Engine lift product illustration" style="background:linear-gradient(180deg,#d9d9d9,#c6b08a)"></div></div>
  <div class="product-img" style="left:475px"><div role="img" aria-label="Wind shovel product illustration" style="background:linear-gradient(90deg,#bdbdbd,#8f8f8f)"></div></div>
  <div class="product-img" style="left:750px"><div role="img" aria-label="Urine bottle product illustration" style="background:linear-gradient(135deg,#e0e0e0,#3d5fd9)"></div></div>

  <div class="arrow-btn" style="left:185px"><svg width="8" height="8" viewBox="0 0 8 8"><path d="M5 1L2 4l3 3" stroke="#fff" fill="none"/></svg></div>
  <div class="arrow-btn" style="left:984px"><svg width="8" height="8" viewBox="0 0 8 8"><path d="M3 1l3 3-3 3" stroke="#fff" fill="none"/></svg></div>

  <div class="product-name" style="left:200px">ENGINE LIFT</div>
  <div class="product-name" style="left:475px">WIND SHOVEL</div>
  <div class="product-name" style="left:750px">URINE BOTTLE</div>

  <div class="btn btn-orange" style="left:216px;top:385px;width:124px;height:31px">Buy On Quorvin</div>
  <div class="btn btn-dark" style="left:347px;top:385px;width:87px;height:31px">More Info</div>
  <div class="btn btn-orange" style="left:491px;top:385px;width:124px;height:31px">Buy On Quorvin</div>
  <div class="btn btn-dark" style="left:622px;top:385px;width:87px;height:31px">More Info</div>
  <div class="btn btn-orange" style="left:766px;top:385px;width:124px;height:31px">Buy On Quorvin</div>
  <div class="btn btn-dark" style="left:897px;top:385px;width:87px;height:31px">More Info</div>
</section>

<section class="blogs">
  <h2 class="section-title" style="top:46px;color:var(--dark)">Latest blogs</h2>
  <div class="underline" style="left:575px;top:94px"></div>

  <div class="blog-img" role="img" aria-label="Golf bag on a trolley on the grass" style="left:200px;top:157px;width:181px;height:181px;background:linear-gradient(160deg,#7aa24a,#3e3e3e 60%,#6d9a3c)"></div>
  <div class="blog-title" style="left:200px;top:355px;width:190px">Contrary to Popular Lorem Belief, Lorem Ipsum</div>
  <div class="blog-text" style="left:200px;top:398px;width:170px">There are many variations of passages of lorem Ipsum avail-able, but the majority have suffered alteration ...</div>
  <div class="read-more" style="left:200px;top:469px">Read More &rarr;</div>

  <div class="blog-img" role="img" aria-label="Angler in an orange jacket fishing by a forest stream" style="left:430px;top:127px;width:338px;height:299px;background:linear-gradient(120deg,#6e7a5c,#4d5540 45%,#c96a2a 65%,#5c6350)"></div>
  <div class="blog-box">
    <div class="blog-title" style="left:30px;top:31px;width:227px">Contrary to Popular Lorem Belief, Lorem Ipsum</div>
    <div class="blog-text" style="left:15px;top:75px;width:257px">There are many variations of passages of lorem Ipsum available, but the majority have suffered alteration ...</div>
    <div class="read-more" style="left:0;top:133px;width:287px">Read More &rarr;</div>
  </div>

  <div class="blog-img" role="img" aria-label="Person stepping onto a boat at a marina" style="left:818px;top:157px;width:181px;height:181px;background:linear-gradient(160deg,#d8dde2,#8e969c 55%,#c9ccce)"></div>
  <div class="blog-title" style="left:818px;top:355px;width:190px">Contrary to Popular Lorem Belief, Lorem Ipsum</div>
  <div class="blog-text" style="left:818px;top:398px;width:170px">There are many variations of passages of lorem Ipsum avail-able, but the majority have suffered alteration ...</div>
  <div class="read-more" style="left:818px;top:469px">Read More &rarr;</div>

  <div class="btn btn-dark" style="left:544px;top:540px;width:111px;height:31px">View All Blog</div>
</section>

<footer class="site-footer">
  <div class="footer-title" style="left:200px;top:64px">About Kestrel Outdoor</div>
  <p class="footer-text" style="left:200px;top:91px;width:350px">Lorem ipsum dolor sit amet, consectetur adipiscing elit, sed do eiusmod tempor incididunt ut labore et dolore magna aliqua. Ut enim ad minim veniam, quis nostrud exercitation ullamco laboris nisi ut aliquip ex ea commodo consequat Duis aute irure dolor ...</p>
  <div class="btn btn-orange" style="left:200px;top:171px;width:124px;height:31px">Discover More</div>

  <div class="footer-title" style="left:612px;top:61px">Contact Us</div>
  <div class="abs" style="left:612px;top:91px;font-size:14px;display:flex;gap:8px;align-items:center"><svg width="12" height="12" viewBox="0 0 24 24"><path d="M6 3l3 5-2 2a12 12 0 006 6l2-2 5 3-2 4C10 21 3 14 3 5z" fill="none" stroke="#f7931e" stroke-width="2"/></svg>123-456-7890</div>
  <div class="abs" style="left:612px;top:116px;font-size:11px;color:#cfcfcf;display:flex;gap:10px;align-items:center"><svg width="11" height="11" viewBox="0 0 24 24"><rect x="3" y="6" width="18" height="13" rx="2" fill="none" stroke="#f7931e" stroke-width="2"/></svg>info@kestreloutdoor.com</div>
  <div class="social" style="left:612px;top:172px"><i aria-label="Social link"></i><i class="on" aria-label="Social link"></i><i aria-label="Social link"></i></div>

  <div class="footer-title" style="left:818px;top:61px">Quick Links</div>
  <div class="quick-links">Home<br>About Us<br>Boat<br>Tarpaulin<br>Fishing<br>Golf<br>Blog<br>Contact Us</div>
  <svg class="abs" style="left:991px;top:62px" width="16" height="18" viewBox="0 0 16 18"><path d="M8 0l8 18-8-5-8 5z" fill="#f7931e"/></svg>

  <div class="divider"></div>
  <div class="copyright">&copy; 2021 <span style="color:var(--orange)">Kestrel Outdoor.</span> All Right Reserved</div>
</footer>

</body>
</html>
```